I need to redesign this website. Modern Fun Professional Redesign For www.JollyPerkHub.com = New Name www.ClaimVouchly.com

Use existing content as it is on website exactly and we will revise after initial mock ups.

The new name will be ClaimVouchly.com please make a quick logo for this site too while redesigning.

Make it look like an official website....

Target Market(s)

Consumers that are redeeming certificates that businesses gave to them as a gift for customer loyalty,e tc.

Industry/Entity Type

It Professional

Logo Text

www.ClaimVouchly.com

Number of Pages Required

4 page

Colors

Designer to choose colors to be used in the design.

Requirements
Must have
• Must look professional, build trust and credibility.
Nice to have
• open
Should not have
• open

```html
<!DOCTYPE html>
<html lang="en">
<head>
<meta charset="utf-8">
<title>ClaimVouchly – The Redemption Source</title>
<link rel="stylesheet" href="https://fonts.googleapis.com/css2?family=Roboto:wght@400;500;700&family=Roboto+Condensed:wght@700&display=swap">
<style>
:root{
  --teal:#5bc5cf;
  --orange:#f07121;
  --gold:#d4a02a;
  --amber:#f0a81e;
  --green:#12875a;
  --green-light:#c9ecd9;
  --ink:#1f1f1f;
  --text:#444;
  --footer:#1b1b1b;
  --white:#fff;
}
*{box-sizing:border-box;margin:0;padding:0}
html,body{width:686px;height:1200px;overflow:hidden;background:var(--white)}
body{position:relative;font-family:'Roboto',Arial,sans-serif;color:var(--text)}
.abs{position:absolute}

/* header */
.top-rule{left:0;top:0;width:686px;height:2px;background:var(--teal)}
.brand{left:92px;top:17px;display:flex;align-items:center;gap:7px}
.brand-mark{width:12px;height:12px;background:var(--teal)}
.brand-name{font-size:15px;font-weight:500;color:var(--ink);line-height:1}
.nav{top:18px;height:17px;font-size:6.5px;color:var(--ink);display:flex;align-items:center;font-weight:500;letter-spacing:.2px}
.nav.active{border:1px solid var(--orange);padding:0 10px}

/* hero */
.hero{left:0;top:50px;width:686px;height:256px;background:linear-gradient(180deg,#6d6d6d 0%,#9a9a9a 45%,#555 80%,#3a3a3a 100%)}
.hero-title{left:0;top:116px;width:686px;text-align:center;font-family:'Roboto Condensed',Arial,sans-serif;font-size:29px;font-weight:700;color:var(--teal);letter-spacing:-.5px}
.hero-sub{left:0;top:153px;width:686px;text-align:center;font-size:7.6px;font-weight:700;color:var(--amber)}
.search{left:230px;top:181px;width:193px;height:20px;border:1.5px solid var(--white);display:flex;align-items:center;padding-left:6px}
.go{left:425px;top:180px;width:28px;height:22px;background:var(--teal);color:var(--white);font-family:'Roboto Condensed',Arial,sans-serif;font-weight:700;font-size:11px;display:flex;align-items:center;justify-content:center}

/* services */
.service{width:180px;text-align:center}
.service-icon{width:60px;height:60px;border-radius:50%;background:var(--orange);margin:0 auto;display:flex;align-items:center;justify-content:center}
.service-title{font-size:10px;font-weight:500;color:var(--teal);margin-top:7px}
.service-lead{font-size:7.5px;color:var(--ink);margin-top:9px}
.service-body{font-size:5.8px;line-height:8.5px;color:var(--text);margin-top:9px;padding:0 20px}
.btn-dark{display:inline-flex;align-items:center;gap:3px;margin-top:17px;background:var(--ink);color:var(--white);font-size:5.8px;height:19px;padding:0 8px;border-radius:1px}

/* welcome band */
.band{left:0;top:526px;width:686px;height:215px;background:linear-gradient(90deg,#168a5b,#0f7f52 60%,#148c5c)}
.band-photo{left:92px;top:551px;width:187px;height:212px;background:var(--green-light);padding:4px}
.band-photo div{width:100%;height:100%;background:linear-gradient(160deg,#e7e2d4,#c9b9a3 45%,#8f8a8a 100%)}
.welcome-title{left:298px;top:550px;font-size:13px;color:var(--white);font-weight:500}
.welcome-body{left:298px;top:573px;width:296px;font-size:5.8px;line-height:9.2px;color:#e6f4ec}
.col-title{font-size:9.5px;color:var(--white);font-weight:500}
.col-body{font-size:5.6px;line-height:8.6px;color:#e6f4ec;text-align:justify;margin-top:6px}
.col-body strong{color:var(--white)}
.btn-outline{display:inline-flex;align-items:center;gap:4px;margin-top:11px;border:1px solid var(--white);color:var(--white);font-size:5.6px;font-weight:500;height:18px;padding:0 9px}

/* testimonials */
.section-title{left:0;top:785px;width:686px;text-align:center;font-family:'Roboto Condensed',Arial,sans-serif;font-size:17px;font-weight:700;color:var(--ink)}
.section-rule{left:328px;top:809px;width:29px;height:2px;background:var(--gold)}
.avatar{border-radius:50%;background:radial-gradient(circle at 50% 40%,#d9c2a8,#a88a70);border:2px solid var(--gold)}
.avatar.featured{border:2.5px solid var(--teal);background:radial-gradient(circle at 50% 40%,#b8b3ad,#6f7479)}
.person{width:170px;text-align:center}
.person-name{display:flex;align-items:center;justify-content:center;gap:5px;font-size:7.5px;color:var(--ink)}
.person-name span{width:23px;height:1px;background:var(--ink)}
.quote{font-size:5.9px;line-height:10.3px;color:var(--text);margin-top:4px;padding:0 23px}
.dot{top:1028px;height:3px;width:26px;background:var(--teal)}
.dot.on{background:#555}

/* footer */
.footer{left:0;top:1066px;width:686px;height:110px;background:linear-gradient(180deg,#222,var(--footer))}
.contact-box{width:53px;height:46px;background:var(--teal);border-radius:2px;display:flex;align-items:center;justify-content:center;top:1098px}
.contact-text{font-size:9px;color:#cfcfcf}
.contact-text.small{font-size:7px;line-height:10px}
.copyright{left:0;top:1176px;width:686px;height:24px;background:var(--orange);color:var(--white);font-size:6.5px;display:flex;align-items:center;justify-content:center}
</style>
</head>
<body>

<header>
  <div class="abs top-rule"></div>
  <div class="abs brand"><span class="brand-mark"></span><span class="brand-name">ClaimVouchly</span></div>
  <nav>
    <div class="abs nav active" style="left:412px;width:43px;justify-content:center">HOME</div>
    <div class="abs nav" style="left:459px">CONTACT US</div>
    <div class="abs nav" style="left:513px">TESTIMONIALS</div>
    <div class="abs nav" style="left:572px">TERMS</div>
  </nav>
</header>

<section>
  <div class="abs hero" role="img" aria-label="Black and white airport terminal with a traveller pulling a suitcase past a window and a plane overhead"></div>
  <h1 class="abs hero-title">THE REDEMPTION SOURCE</h1>
  <p class="abs hero-sub">PLEASE ENTER A VALID CERTIFICATE ID IN THE FORM BELOW</p>
  <div class="abs search">
    <svg width="10" height="10" viewBox="0 0 10 10"><circle cx="4" cy="4" r="3" fill="none" stroke="#fff" stroke-width="1.4"/><line x1="6.2" y1="6.2" x2="9" y2="9" stroke="#fff" stroke-width="1.6"/></svg>
  </div>
  <div class="abs go">GO</div>
</section>

<section>
  <div class="abs service" style="left:70px;top:327px">
    <div class="service-icon">
      <svg width="24" height="28" viewBox="0 0 24 28" fill="#fff"><rect x="3" y="5" width="18" height="23"/><g fill="#f07121"><rect x="6" y="8" width="3" height="3"/><rect x="10.5" y="8" width="3" height="3"/><rect x="15" y="8" width="3" height="3"/><rect x="6" y="13" width="3" height="3"/><rect x="10.5" y="13" width="3" height="3"/><rect x="15" y="13" width="3" height="3"/><rect x="6" y="18" width="3" height="3"/><rect x="15" y="18" width="3" height="3"/><rect x="10" y="21" width="4" height="7"/></g><circle cx="8" cy="2" r="1.2"/><circle cx="12" cy="2" r="1.2"/><circle cx="16" cy="2" r="1.2"/></svg>
    </div>
    <div class="service-title">Hotel</div>
    <div class="service-lead">Lorem Ipsum is simply</div>
    <p class="service-body">Lorem Ipsum is simply dummy text of the print been the industry's standard dummy maketype software like Layout Studio including versions of Lorem Ipsum.</p>
    <span class="btn-dark"><svg width="6" height="6" viewBox="0 0 6 6"><circle cx="3" cy="3" r="3" fill="#fff"/><path d="M3 1.5v3M1.5 3h3" stroke="#1f1f1f" stroke-width="1"/></svg>Read More</span>
  </div>
  <div class="abs service" style="left:249px;top:327px">
    <div class="service-icon">
      <svg width="30" height="28" viewBox="0 0 30 28"><circle cx="12" cy="16" r="10" fill="none" stroke="#fff" stroke-width="2"/><path d="M2 16h20M12 6c-4 5-4 15 0 20M12 6c4 5 4 15 0 20" stroke="#fff" stroke-width="1.5" fill="none"/><path d="M15 9l13-7 1 2-9 6 3 4-2 1-4-3z" fill="#fff"/></svg>
    </div>
    <div class="service-title">Flight</div>
    <div class="service-lead">Lorem Ipsum is simply</div>
    <p class="service-body">Lorem Ipsum is simply dummy text of the print been the industry's standard dummy maketype software like Layout Studio including versions of Lorem Ipsum.</p>
    <span class="btn-dark"><svg width="6" height="6" viewBox="0 0 6 6"><circle cx="3" cy="3" r="3" fill="#fff"/><path d="M3 1.5v3M1.5 3h3" stroke="#1f1f1f" stroke-width="1"/></svg>Read More</span>
  </div>
  <div class="abs service" style="left:431px;top:327px">
    <div class="service-icon">
      <svg width="26" height="30" viewBox="0 0 26 30" fill="#fff"><circle cx="15" cy="4" r="3"/><path d="M12 9h5l3 8-2 1-2-4-1 6 4 9h-3l-3-7-2 7h-3l3-12z"/><rect x="2" y="16" width="7" height="9" rx="1"/></svg>
    </div>
    <div class="service-title">Trip</div>
    <div class="service-lead">Lorem Ipsum is simply</div>
    <p class="service-body">Lorem Ipsum is simply dummy text of the print been the industry's standard dummy maketype software like Layout Studio including versions of Lorem Ipsum.</p>
    <span class="btn-dark"><svg width="6" height="6" viewBox="0 0 6 6"><circle cx="3" cy="3" r="3" fill="#fff"/><path d="M3 1.5v3M1.5 3h3" stroke="#1f1f1f" stroke-width="1"/></svg>Read More</span>
  </div>
</section>

<section>
  <div class="abs band"></div>
  <div class="abs band-photo"><div role="img" aria-label="Happy family with suitcases walking through an airport terminal"></div></div>
  <h2 class="abs welcome-title">Welcome to ClaimVouchly</h2>
  <p class="abs welcome-body">Lorem Ipsum is simply dummy text of the printing and typesetting industry. Lorem Ipsum has been ndustry's Ipsum.Lorem Ipsum is simply dummy text of the printing and typesetting industry.been remaining essentially more recently with desktop publishing software like Layout Studio including versionsLorem Ipsum.Lorem ever since the 1500s, when an unknown printer took a galley of type and scrambled it to make a type specimen book.</p>
  <div class="abs" style="left:298px;top:630px;width:128px">
    <h3 class="col-title">Company History</h3>
    <p class="col-body">Lorem Ipsum is simply dummy best text of the printing and typesetting industry. Lorem Ipsum has been the industry's standard dummy text a type specimen book. It has survived not only five centuries, but also the leap</p>
    <span class="btn-outline">READ MORE <svg width="6" height="6" viewBox="0 0 6 6"><circle cx="3" cy="3" r="3" fill="#fff"/><path d="M2.3 1.6L3.7 3 2.3 4.4" stroke="#12875a" stroke-width="1" fill="none"/></svg></span>
  </div>
  <div class="abs" style="left:466px;top:630px;width:128px">
    <h3 class="col-title">Our Philosophy</h3>
    <p class="col-body">Our goal is to make it easy for you to redeem your certificate and our philosophy is this: <strong>"What good is it to receive a gift certificate if you can't use it?"</strong></p>
    <span class="btn-outline" style="margin-top:19px">READ MORE <svg width="6" height="6" viewBox="0 0 6 6"><circle cx="3" cy="3" r="3" fill="#fff"/><path d="M2.3 1.6L3.7 3 2.3 4.4" stroke="#12875a" stroke-width="1" fill="none"/></svg></span>
  </div>
</section>

<section>
  <h2 class="abs section-title">TESTIMONIALS</h2>
  <div class="abs section-rule"></div>

  <div class="abs avatar" style="left:132px;top:844px;width:84px;height:84px" role="img" aria-label="Portrait of customer Mara T."></div>
  <div class="abs avatar featured" style="left:286px;top:834px;width:104px;height:104px" role="img" aria-label="Portrait of customer Jo Ellen P."></div>
  <div class="abs avatar" style="left:475px;top:848px;width:77px;height:77px" role="img" aria-label="Portrait of customer Helen W."></div>

  <div class="abs person" style="left:89px;top:950px">
    <div class="person-name"><span></span>Mara T.<span></span></div>
    <p class="quote">Irene was a "saving grace." She followed up and helped me book the vacation and air fare. Irene was positive and did everything she promised to do.</p>
  </div>
  <div class="abs person" style="left:253px;top:950px">
    <div class="person-name"><span></span>Jo Ellen P.<span></span></div>
    <p class="quote">Daniel was able to put together our flight schedule. He was very patient with us and diligent in working out all the changes I was requesting. Thank you, Dan.</p>
  </div>
  <div class="abs person" style="left:428px;top:950px">
    <div class="person-name"><span></span>Helen W.<span></span></div>
    <p class="quote">Our vacation was great!!!! We stayed at the Grand Aurelia. And we had a lot of fun. We do not have any pictures as everyone else took them. We celebrated our grandson's 21st birthday.</p>
  </div>

  <div class="abs dot on" style="left:294px"></div>
  <div class="abs dot" style="left:326px"></div>
  <div class="abs dot" style="left:356px"></div>
</section>

<footer>
  <div class="abs footer" role="img" aria-label="Faint dark map of the United States"></div>
  <div class="abs contact-box" style="left:92px">
    <svg width="18" height="18" viewBox="0 0 24 24"><path d="M6.6 10.8a15 15 0 006.6 6.6l2.2-2.2a1 1 0 011-.25 11.4 11.4 0 003.6.57 1 1 0 011 1V20a1 1 0 01-1 1A17 17 0 013 4a1 1 0 011-1h3.5a1 1 0 011 1c0 1.25.2 2.45.57 3.6a1 1 0 01-.25 1z" fill="#1b1b1b"/></svg>
  </div>
  <div class="abs contact-text" style="left:154px;top:1115px">0412 608 357</div>
  <div class="abs contact-box" style="left:254px">
    <svg width="22" height="16" viewBox="0 0 22 16"><rect x="1" y="1" width="20" height="14" fill="none" stroke="#1b1b1b" stroke-width="2"/><path d="M1 1l10 8 10-8" fill="none" stroke="#1b1b1b" stroke-width="2"/></svg>
  </div>
  <div class="abs contact-text" style="left:314px;top:1115px">info@claimvouchly.com</div>
  <div class="abs contact-box" style="left:438px">
    <svg width="14" height="20" viewBox="0 0 14 20"><path d="M7 0a7 7 0 017 7c0 5-7 13-7 13S0 12 0 7a7 7 0 017-7z" fill="#1b1b1b"/><circle cx="7" cy="7" r="2.5" fill="#5bc5cf"/></svg>
  </div>
  <div class="abs contact-text small" style="left:500px;top:1111px">2245 Marlow Park Ave Ste B<br>#118 Fairview, Ca 90210</div>
  <div class="abs copyright">Copyright 2017, claimvouchly.com, All Rights Reserved.</div>
</footer>

</body>
</html>
```